Business Card Design Project

Hello
I want a Simple Business card that uses the company logo that is easily reasonable but looks professional as I am an IT Services company and would look to share these cards with prospective clients.
The details are:
Kestrel Arc Solutions
14 Morrow Lane
Birmingham
B7 4QX
Telephone 0845 217 6640
I would like my name Oliver Hastings and my title Director on the card.
Target Market(s)
IT Professionals
Industry/Entity Type
Business

```html
<!DOCTYPE html>
<html lang="en">
<head>
<meta charset="utf-8">
<title>Kestrel Arc Solutions – Business Card</title>
<link rel="stylesheet" href="https://fonts.googleapis.com/css2?family=Noto+Sans:wght@400&display=swap">
<style>
  :root {
    --bg-light: #fbfde6;
    --bg-mid: #e2f0b8;
    --bg-deep: #b9dc93;
    --brand-ink: #231f20;
    --brand-dot: #8cc63f;
    --detail-green: #3f5c0c;
    --name-ink: #0c0c0c;
  }
  * { margin: 0; padding: 0; box-sizing: border-box; }
  html, body {
    width: 1200px;
    height: 686px;
    overflow: hidden;
    background: var(--bg-light);
  }
  .business-card {
    position: relative;
    width: 1200px;
    height: 686px;
    overflow: hidden;
    font-family: "Noto Sans", sans-serif;
    font-weight: 400;
  }
  .card-backdrop {
    position: absolute;
    inset: 0;
    background:
      radial-gradient(ellipse 70% 80% at 92% 40%, var(--bg-light) 0%, rgba(251,253,230,0) 70%),
      linear-gradient(100deg, var(--bg-deep) 0%, var(--bg-mid) 45%, var(--bg-light) 100%);
  }
  .brand {
    position: absolute;
    left: 0;
    top: 60px;
    width: 1212px;
    text-align: center;
  }
  .brand-mark {
    display: block;
    margin: 0 auto 26px;
  }
  .brand-name {
    font-size: 60px;
    line-height: 1;
    color: var(--brand-ink);
    letter-spacing: -0.5px;
  }
  .address {
    position: absolute;
    left: 33px;
    top: 362px;
    width: 500px;
    text-align: center;
    color: var(--detail-green);
    font-size: 50px;
    line-height: 67px;
  }
  .phone {
    position: absolute;
    left: 57px;
    top: 600px;
    color: var(--detail-green);
    font-size: 50px;
    line-height: 1.2;
  }
  .person {
    position: absolute;
    left: 700px;
    top: 392px;
    width: 440px;
    text-align: center;
  }
  .person-name {
    color: var(--name-ink);
    font-size: 68px;
    line-height: 91px;
  }
  .person-title {
    color: var(--detail-green);
    font-size: 43px;
    line-height: 1.2;
  }
</style>
</head>
<body>
  <main class="business-card">
    <div class="card-backdrop" role="img" aria-label="Soft green background with blurred light circles"></div>

    <header class="brand">
      <svg class="brand-mark" width="110" height="110" viewBox="0 0 110 110" aria-hidden="true">
        <circle cx="55" cy="55" r="55" fill="var(--brand-dot)"/>
      </svg>
      <div class="brand-name">Kestrel Arc Solutions</div>
    </header>

    <address class="address" style="font-style: normal;">
      14 Morrow Lane<br>
      Birmingham<br>
      B7 4QX
    </address>

    <p class="phone">0845 217 6640</p>

    <section class="person">
      <p class="person-name">Oliver<br>Hastings</p>
      <p class="person-title">director</p>
    </section>
  </main>
</body>
</html>
```